Help us stand out from the crowd - Pellingham Row

We are a luxury watch business and are looking to develop our own paperwork that we can issue with our watches etc. I am looking for the following documents to be designed: Invoice, Warranty card, Insurance valuation, instruction booklet and a small folder to keep it all in. Need it to be small though. I have attached some images of my friends ones that look fantastic.

Target Market(s)

High net worth watch enthusiasts

Requirements
Must have
• Must be clean, precise and very easy on the eye. Think Vorla but underpinned with a classic british feel.
Should not have
• Shouldn't be dark.

```html
<!DOCTYPE html>
<html lang="en">
<head>
<meta charset="utf-8">
<title>Pellingham Row – Stationery</title>
<link href="https://fonts.googleapis.com/css2?family=Cinzel:wght@400;600&family=Montserrat:wght@400;500;600&family=Open+Sans:wght@400;600;700&family=Roboto+Condensed:wght@400;700&family=Dancing+Script:wght@500&display=swap" rel="stylesheet">
<style>
:root{
  --page-bg:#eceef1;
  --paper:#ffffff;
  --ink:#1e1e1e;
  --ink-soft:#5a5a5a;
  --ink-mute:#7a7a7a;
  --rule:#8c8c8c;
  --band:#5b5b5b;
  --band-dark:#474747;
  --stripe:#efefef;
  --silver-1:#f4f4f4;
  --silver-2:#d9d9d9;
  --card-dark:#2b2b2b;
}
*{box-sizing:border-box;margin:0;padding:0}
html,body{width:1200px;height:1024px;overflow:hidden}
body{background:var(--page-bg);position:relative;font-family:"Montserrat",sans-serif;color:var(--ink)}

/* Guarantee card */
.guarantee-card{position:absolute;left:90px;top:433px;width:322px;height:184px;border-radius:12px;overflow:hidden;box-shadow:0 4px 14px rgba(0,0,0,.18)}
.card-texture{position:absolute;inset:0;background:linear-gradient(115deg,var(--silver-2) 0%,var(--silver-1) 35%,#ffffff 55%,var(--silver-2) 100%)}
.card-title{position:absolute;left:0;right:0;top:14px;text-align:center;font:700 14px "Open Sans",sans-serif;color:var(--ink);letter-spacing:.2px}
.card-title-rule{position:absolute;left:79px;width:164px;top:32px;border-top:1px solid var(--ink)}
.card-sub{position:absolute;left:0;right:0;top:34px;text-align:center;font:600 6.5px "Open Sans",sans-serif}
.card-field{position:absolute;left:32px;font:700 6.8px "Open Sans",sans-serif;display:flex;align-items:flex-end;gap:2px}
.card-field .line{border-bottom:.8px solid #444;height:6px}
.card-band{position:absolute;left:14px;top:139px;width:293px;height:37px;background:var(--card-dark);border-radius:4px;color:#fff}
.card-band .contact{position:absolute;top:6px;font:400 5.6px "Roboto Condensed",sans-serif;line-height:8.4px}
.card-band .contact svg{width:5px;height:5px;vertical-align:-0.5px;margin-right:2px}
.card-brand{position:absolute;left:172px;top:8px;width:112px;text-align:center;font:500 9px "Montserrat",sans-serif;color:#fff}
.card-tagline{position:absolute;left:172px;width:112px;top:22px;text-align:center;font:400 5px "Montserrat",sans-serif;color:#ddd}

.caption{position:absolute;font:400 17px "Open Sans",sans-serif;color:#3b4550;text-align:center}

/* Invoice */
.invoice{position:absolute;left:448px;top:54px;width:633px;height:884px;background:var(--paper);box-shadow:0 6px 20px rgba(0,0,0,.15)}
.brand-name{position:absolute;left:44px;top:44px;width:207px;text-align:center;font:500 17px "Montserrat",sans-serif;color:var(--ink)}
.brand-tagline{position:absolute;left:44px;top:69px;width:207px;text-align:center;font:400 8.5px "Montserrat",sans-serif;color:var(--ink-soft)}
.header-divider{position:absolute;left:262px;top:32px;height:64px;border-left:1px solid #aaa}
.contact-block{position:absolute;left:272px;top:32px;font:400 9.6px "Montserrat",sans-serif;color:var(--ink-soft);line-height:13.1px;font-style:normal}
.contact-block svg{width:8px;height:8px;vertical-align:-1px;margin-right:5px;fill:var(--ink-soft)}
.doc-title{position:absolute;right:36px;top:46px;font:600 30px "Cinzel",serif;color:var(--ink);letter-spacing:.5px}

.info-box{position:absolute;left:36px;top:141px;width:561px;height:62px;border:1px solid var(--rule);display:flex}
.info-box > div{flex:0 0 187px;border-right:1px solid var(--rule);padding:7px 11px;font:600 10px "Montserrat",sans-serif;color:var(--ink-mute)}
.info-box > div:last-child{border-right:none;padding:7px 7px}
.meta-row{display:flex;justify-content:space-between;font-size:9.8px;line-height:17px}
.meta-row span:last-child{font-weight:400}

.ship-box{position:absolute;left:36px;top:223px;width:561px;height:61px;border:1px solid var(--rule);border-top:none;display:flex}
.ship-box > div{flex:0 0 187px;border-right:1px solid var(--rule)}
.ship-box > div:last-child{border-right:none}
.band-head{height:28px;background:linear-gradient(90deg,var(--band),var(--band-dark));color:#fff;font:400 10.4px "Montserrat",sans-serif;display:flex;align-items:center;justify-content:center;border-right:1px solid #ddd}

.items{position:absolute;left:36px;top:299px;width:561px;height:306px;border:1px solid var(--rule)}
.items table{width:100%;border-collapse:collapse}
.items th{height:43px;background:linear-gradient(90deg,var(--band),var(--band-dark));color:#fff;font:700 9.6px "Roboto Condensed",sans-serif;border-right:1px solid #ddd}
.items td{height:26.2px;border-right:1px solid #b5b5b5}
.items th:last-child,.items td:last-child{border-right:none}
.items tr:nth-child(even) td{background:var(--stripe)}

.totals{position:absolute;left:363px;top:605px;width:234px;border-left:1px solid var(--rule);border-right:1px solid var(--rule)}
.totals div{height:25.5px;padding-left:10px;font:400 12.5px "Roboto Condensed",sans-serif;color:var(--ink-mute);display:flex;align-items:center;letter-spacing:.2px}
.totals div:nth-child(even){background:var(--stripe)}
.grand-total{position:absolute;left:363px;top:709px;width:234px;height:38px;border:1.5px solid #444;padding-left:10px;display:flex;align-items:center;font:700 15px "Roboto Condensed",sans-serif;color:var(--ink-soft)}

.signature-mark{position:absolute;left:90px;top:674px;width:140px;text-align:center;font:500 25px "Dancing Script",cursive;color:var(--ink)}
.signature-rule{position:absolute;left:90px;top:709px;width:140px;border-top:1px solid #aaa}
.signature-label{position:absolute;left:90px;top:712px;width:140px;text-align:center;font:400 13px "Roboto Condensed",sans-serif;color:var(--ink-mute)}

.terms{position:absolute;left:35px;top:758px;list-style:none;font:400 12px "Roboto Condensed",sans-serif;color:var(--ink-mute);line-height:17px}
.payment{position:absolute;left:390px;top:779px;width:180px;text-align:center;font:400 12.5px "Roboto Condensed",sans-serif;color:var(--ink-soft);line-height:17px}
.payment strong{font-weight:700;font-size:13px}
.closing-bar{position:absolute;left:306px;top:846px;width:20px;height:3px;background:var(--ink)}
.closing{position:absolute;left:0;right:0;top:854px;text-align:center;font:italic 400 14px "Open Sans",sans-serif;color:var(--ink-soft)}
</style>
</head>
<body>

<section class="guarantee-card">
  <div class="card-texture" role="img" aria-label="Brushed silver background with a faint repeating watch-face pattern"></div>
  <h2 class="card-title">GUARANTEE CARD</h2>
  <div class="card-title-rule"></div>
  <p class="card-sub">Please fill in the details on the Guarantee Card</p>
  <div class="card-field" style="top:52px">Name<span class="line" style="width:233px"></span></div>
  <div class="card-field" style="top:67px">Model<span class="line" style="width:231px"></span></div>
  <div class="card-field" style="top:83px">Serial Number<span class="line" style="width:204px"></span></div>
  <div class="card-field" style="top:98px">Dial<span class="line" style="width:240px"></span></div>
  <div class="card-field" style="top:113px">Date of Purchase<span class="line" style="width:78px"></span><span style="margin-left:2px">Dealer Sign/Seal</span><span class="line" style="width:53px"></span></div>
  <div class="card-band">
    <div class="contact" style="left:11px">
      <div><svg viewBox="0 0 10 10"><path fill="#fff" d="M2 1l2 2-1 1.2a6 6 0 0 0 2.8 2.8L7 6l2 2-1.2 1.2C4.5 9 1 5.5.8 2.2z"/></svg>+31 (6) 20418855</div>
      <div><svg viewBox="0 0 10 10"><path fill="#fff" d="M0 2h10v6H0z"/></svg>sales@pellinghamrow.com</div>
      <div><svg viewBox="0 0 10 10"><circle cx="5" cy="5" r="4.3" fill="none" stroke="#fff"/><path d="M.7 5h8.6M5 .7c-2.4 2.8-2.4 5.8 0 8.6M5 .7c2.4 2.8 2.4 5.8 0 8.6" stroke="#fff" fill="none" stroke-width=".7"/></svg>www.pellinghamrow.com</div>
    </div>
    <div class="contact" style="left:95px">
      <div>Lindenkade 27</div><div>4811 PX Breda</div><div>Netherlands</div>
    </div>
    <div class="card-brand">Pellingham Row</div>
    <div class="card-tagline">Fine watches, kept with care</div>
  </div>
</section>
<p class="caption" style="left:90px;width:322px;top:636px">Guarantee Card</p>

<section class="invoice">
  <div class="brand-name">Pellingham Row</div>
  <div class="brand-tagline">Fine watches, kept with care</div>
  <div class="header-divider"></div>
  <address class="contact-block">
    <div>Lindenkade 27</div>
    <div>4811 PX Breda, Netherlands</div>
    <div><svg viewBox="0 0 10 10"><path d="M2 1l2 2-1 1.2a6 6 0 0 0 2.8 2.8L7 6l2 2-1.2 1.2C4.5 9 1 5.5.8 2.2z"/></svg>+31 (6) 20418855</div>
    <div><svg viewBox="0 0 10 10"><path d="M0 2h10v6H0z"/><path d="M0 2l5 3.5L10 2" stroke="#fff" fill="none"/></svg>sales@pellinghamrow.com</div>
    <div><svg viewBox="0 0 10 10"><circle cx="5" cy="5" r="4.3" fill="none" stroke="#5a5a5a"/><path d="M.7 5h8.6M5 .7c-2.4 2.8-2.4 5.8 0 8.6M5 .7c2.4 2.8 2.4 5.8 0 8.6" stroke="#5a5a5a" fill="none" stroke-width=".7"/></svg>www.pellinghamrow.com</div>
  </address>
  <h1 class="doc-title">Invoice</h1>

  <div class="info-box">
    <div>SOLD TO</div>
    <div>SHIP TO</div>
    <div>
      <div class="meta-row"><span>Invoice No.</span><span>120031</span></div>
      <div class="meta-row"><span>Invoice Date</span><span>May 31, 2021</span></div>
      <div class="meta-row"><span>Customer Order No</span><span>31442167</span></div>
    </div>
  </div>

  <div class="ship-box">
    <div><div class="band-head">SALES PERSON</div></div>
    <div><div class="band-head">SHIPPED VIA</div></div>
    <div><div class="band-head" style="border-right:none">TERMS</div></div>
  </div>

  <div class="items">
    <table>
      <thead><tr>
        <th style="width:245px">DESCRIPTION</th>
        <th style="width:82px">QTY ORDERED</th>
        <th style="width:77px">QTY SHIPPED</th>
        <th style="width:62px">UNIT</th>
        <th>AMOUNT</th>
      </tr></thead>
      <tbody>
        <tr><td></td><td></td><td></td><td></td><td></td></tr>
        <tr><td></td><td></td><td></td><td></td><td></td></tr>
        <tr><td></td><td></td><td></td><td></td><td></td></tr>
        <tr><td></td><td></td><td></td><td></td><td></td></tr>
        <tr><td></td><td></td><td></td><td></td><td></td></tr>
        <tr><td></td><td></td><td></td><td></td><td></td></tr>
        <tr><td></td><td></td><td></td><td></td><td></td></tr>
        <tr><td></td><td></td><td></td><td></td><td></td></tr>
        <tr><td></td><td></td><td></td><td></td><td></td></tr>
        <tr><td></td><td></td><td></td><td></td><td></td></tr>
      </tbody>
    </table>
  </div>

  <div class="totals">
    <div>SUBTOTAL</div>
    <div>SALES TAX</div>
    <div>PAYMENTS/CREDITS</div>
    <div>BALANCE DUE</div>
  </div>
  <div class="grand-total">TOTAL</div>

  <div class="signature-mark">Signature</div>
  <div class="signature-rule"></div>
  <div class="signature-label">Customer Signature</div>

  <ul class="terms">
    <li>• All sales final</li>
    <li>• Old &amp; Antique Rugs SOLD AS IS</li>
    <li>• No Exchange for REFUND, UNLESS STATED OTHERWISE</li>
  </ul>
  <div class="payment"><strong>METHOD OF PAYMENT</strong><br>Debit, Credit, Check, Cash</div>

  <div class="closing-bar"></div>
  <p class="closing">Thank you for your business.</p>
</section>
<p class="caption" style="left:448px;width:633px;top:968px">Invoice Template</p>

</body>
</html>
```